QRV (Guaranteed Project)

**Note: The girl image is not mandatory, that was just an idea, it may even look better with just text and no girl

TEXT (Lorne Bexley and Vantro logos large please):

PEOPLE GET READY (the font from the image below for people get ready looks good, kind of retro)

QRV WEEKEND 2014
SUNDAY MAY 25

430-9pm

QRV after party starts at 9pm-2am

Featuring
LORNE BEXLEY (SF) (use logo, largest name)
VANTRO (Sac) (use logo w/out the text below it, and slightly smaller than lorne bexley)

at K@Z Uptown 2847 J Street 21+

Project Deadline Extended
Reason: The mgr wants to review them and hasn't said yes yet.

Target Market(s)

House/Electronic Music Night Club

Font styles to use
Sans Serif

Colors
ec2027
ffffff

Requirements
Nice to have
• Would look nice with the red background and maybe a reddish filter on the girl

```html
<!DOCTYPE html>
<html lang="en">
<head>
<meta charset="utf-8">
<title>People Get Ready – QRV Weekend 2014</title>
<link rel="stylesheet" href="https://fonts.googleapis.com/css2?family=Orbitron:wght@700;900&family=Michroma&display=swap">
<style>
  :root {
    --red: #ec2027;
    --black: #050203;
    --white: #ffffff;
    --soft-white: #e9e4e4;
  }
  * { margin: 0; padding: 0; box-sizing: border-box; }
  html, body { width: 928px; height: 1200px; overflow: hidden; background: var(--black); }
  .poster {
    position: relative;
    width: 928px;
    height: 1200px;
    overflow: hidden;
    background:
      radial-gradient(ellipse 70% 35% at 20% 55%, rgba(236,32,39,0.55), transparent 70%),
      radial-gradient(ellipse 60% 30% at 85% 50%, rgba(236,32,39,0.35), transparent 70%),
      var(--black);
    color: var(--white);
    font-family: "Michroma", sans-serif;
    text-align: center;
  }
  .hero-photo {
    position: absolute;
    left: 0; top: 0;
    width: 928px; height: 760px;
    background:
      radial-gradient(ellipse 32% 48% at 50% 30%, #d9b7aa 0%, #b88474 45%, transparent 75%),
      radial-gradient(ellipse 60% 60% at 30% 40%, #c4141d 0%, transparent 70%),
      radial-gradient(ellipse 50% 55% at 80% 35%, #a30e16 0%, transparent 70%),
      linear-gradient(180deg, #3a0508 0%, #8c0c13 40%, #2a0306 80%, var(--black) 100%);
    -webkit-mask-image: linear-gradient(180deg, #000 75%, transparent 100%);
    mask-image: linear-gradient(180deg, #000 75%, transparent 100%);
  }
  .headline {
    font-family: "Orbitron", sans-serif;
    font-weight: 900;
    text-shadow: 0 0 18px rgba(0,0,0,0.6);
  }
  .headline .line-one,
  .headline .line-two {
    position: absolute;
    left: 0; right: 0;
    display: block;
  }
  .headline .line-one { top: 652px; font-size: 100px; line-height: 100px; letter-spacing: 18px; padding-left: 18px; }
  .headline .line-two { top: 742px; font-size: 66px; line-height: 66px; letter-spacing: 14px; padding-left: 14px; }
  .event-details {
    position: absolute;
    left: 0; right: 0;
    top: 832px;
    font-size: 17px;
    line-height: 26px;
    color: var(--soft-white);
    letter-spacing: 1px;
  }
  .event-details .time { margin-top: 12px; }
  .divider {
    width: 470px;
    height: 1px;
    margin: 11px auto 10px;
    background: rgba(255,255,255,0.55);
  }
  .lineup {
    position: absolute;
    left: 0; right: 0;
    top: 1010px;
    height: 70px;
    display: flex;
    justify-content: center;
    align-items: center;
    gap: 40px;
  }
  .act { display: flex; align-items: center; gap: 12px; color: var(--white); }
  .act-mark-circle { width: 66px; height: 66px; border-radius: 50%; background: var(--white); opacity: 0.9; }
  .act-mark-square { width: 56px; height: 56px; background: var(--red); }
  .act-name { font-family: "Orbitron", sans-serif; font-weight: 900; line-height: 1; }
  .act-name.headliner { font-size: 31px; text-transform: lowercase; }
  .act-name.secondary { font-size: 36px; text-transform: uppercase; }
  .act-name.venue { font-size: 22px; text-transform: uppercase; }
  .venue-line {
    position: absolute;
    left: 0; right: 0;
    top: 1100px;
    font-size: 17px;
    line-height: 27px;
    color: var(--soft-white);
    letter-spacing: 1px;
  }
</style>
</head>
<body>
  <main class="poster">
    <div class="hero-photo" role="img" aria-label="Photo of a woman with bright eye makeup and blue nails, hands framing her face, on a red sparkling background"></div>

    <h1 class="headline">
      <span class="line-one">PEOPLE</span>
      <span class="line-two">GET READY</span>
    </h1>

    <section class="event-details">
      <p>QRV WEEKEND 2014</p>
      <p>SUNDAY MAY 25</p>
      <p class="time">4:30-9pm</p>
      <p>QRV after party starts at 9pm-2am</p>
      <div class="divider"></div>
      <p class="featuring">Featuring</p>
    </section>

    <section class="lineup">
      <div class="act">
        <span class="act-mark-circle"></span>
        <span class="act-name headliner">lorne bexley</span>
      </div>
      <div class="act">
        <span class="act-name secondary">VANTRO</span>
      </div>
      <div class="act">
        <span class="act-mark-square"></span>
        <span class="act-name venue">K@Z</span>
      </div>
    </section>

    <section class="venue-line">
      <p>House music at its finest</p>
      <p>at K@Z Uptown 2847 J Street 21+</p>
    </section>
  </main>
</body>
</html>
```